Bramwell Hockey Academy

We are are Ice Hockey Development Company that provided on-ice Hockey development services. We need a Landing Page with tabs to direct to individual program pages.
Landing Page
About Page
Winter Program Page
Spring Program Page
Summer Program Page
Team Page
Tournament Page

```html
<!DOCTYPE html>
<html lang="en">
<head>
<meta charset="utf-8">
<title>Bramwell Hockey Academy</title>
<link href="https://fonts.googleapis.com/css2?family=Alegreya+Sans:ital,wght@0,300;0,400;0,500;0,700;0,800;0,900;1,800;1,900&display=swap" rel="stylesheet">
<style>
:root{
  --ink:#111111;
  --dark:#1e1e1e;
  --footer:#191919;
  --green:#0a9a0a;
  --green-bright:#0cb00c;
  --green-deep:#0d6b12;
  --placeholder:#bfbfbf;
  --light:#dfe6e9;
  --paper:#f7f9fa;
  --white:#ffffff;
  --text:#555a5e;
}
*{margin:0;padding:0;box-sizing:border-box}
html,body{width:1200px;height:3820px;overflow:hidden;background:var(--ink)}
body{font-family:"Alegreya Sans",sans-serif;color:var(--white)}
.page{position:relative;width:1200px;height:3820px;overflow:hidden;background:var(--light)}
.abs{position:absolute}
.backdrop{position:absolute;left:0;top:0}

/* header */
.site-header{position:absolute;left:0;top:0;width:1200px;height:89px;background:var(--ink);border-bottom:1px solid #1f3a1f;z-index:3}
.brand{position:absolute;left:100px;top:22px;font-weight:900;font-size:24px;line-height:22px;letter-spacing:.5px;color:var(--white);display:flex;align-items:center;gap:8px}
.brand .mark{width:12px;height:12px;background:var(--green)}
.main-nav{position:absolute;left:494px;top:0;height:89px;display:flex;align-items:center;font-size:15px;text-transform:uppercase;color:#d8d8d8}
.main-nav a{color:inherit;text-decoration:none;position:relative}
.main-nav a.active{color:var(--white)}
.main-nav a.active::before{content:"";position:absolute;left:-18px;right:-18px;top:-42px;height:3px;background:var(--green)}
.main-nav .sep{width:1px;height:22px;background:#555;transform:skewX(-30deg);margin:0 26px}

/* hero */
.hero-photo{left:560px;top:110px;width:640px;height:620px;background:linear-gradient(160deg,rgba(70,74,78,.55),rgba(40,42,45,.25) 60%,rgba(40,42,45,0))}
.hero-title{left:100px;top:236px;font-weight:900;font-style:italic;font-size:78px;line-height:59px;letter-spacing:-4px;text-transform:uppercase}
.hero-title .dot{display:inline-block;width:26px;height:26px;background:var(--green);transform:skewX(-20deg);margin-left:10px}
.hero-text{left:100px;top:472px;width:390px;font-size:13px;line-height:21px;color:#e6e6e6}
.btn-skew{display:flex;align-items:center;justify-content:center;border:1px solid var(--green);transform:skewX(-20deg);font-size:12px}
.btn-skew span{transform:skewX(20deg)}
.hero-btn{left:104px;top:613px;width:152px;height:41px;color:var(--green)}
.partner{top:610px;font-weight:900;font-size:21px;color:var(--white)}
.slider-dots{left:586px;top:804px;display:flex;gap:4px}
.slider-dots i{width:12px;height:12px;background:#8b8f92}
.slider-dots i.on{background:var(--white)}

.category{width:506px;height:245px;background:var(--placeholder)}
.ph-label{position:absolute;font-family:Arial,sans-serif;color:#111;line-height:1}
.category .ph-label{left:128px;top:40px;font-size:66px}
.category h3{position:absolute;left:36px;top:34px;font-weight:800;font-size:24px;line-height:22px;text-transform:uppercase;color:var(--white);width:250px}
.category p{position:absolute;left:36px;top:92px;width:255px;font-size:11px;line-height:19px;color:var(--white)}
.category .see{position:absolute;left:44px;top:190px;font-size:11px;font-weight:700;color:var(--white);padding-bottom:8px;border-bottom:1px solid rgba(255,255,255,.5)}
.category.dark h3,.category.dark p{color:#1b1b1b}
.category.dark p em{color:#0c7a0c;font-style:normal}

/* about */
.section-title{left:0;width:1200px;text-align:center;top:1428px;font-weight:700;font-size:39px;color:#111;text-transform:uppercase}
.title-bar{left:567px;top:1489px;width:66px;height:4px;background:#a7a7a7}
.about-text{left:150px;width:900px;top:1510px;text-align:center;font-size:14px;line-height:20px;color:var(--text)}
.tile{top:1584px;width:322px;height:295px;background:var(--white)}
.tile .ph{position:absolute;left:7px;top:7px;width:308px;height:226px;background:var(--placeholder);border:1px solid #aaa}
.tile .ph-label{left:78px;top:98px;font-size:38px}
.tile .caption{position:absolute;left:17px;top:260px;font-size:14px;color:#6b6b6b}
.tile .likes{position:absolute;right:18px;top:261px;font-size:9px;color:#999;display:flex;gap:4px;align-items:center}

.band{left:0;top:1934px;width:1200px;height:136px;background:var(--placeholder)}
.band .ph-label{left:468px;top:42px;font-size:60px}

/* performance */
.perf-bg{left:0;top:2070px;width:1200px;height:440px;background:var(--paper)}
.perf-title{left:83px;top:2073px;font-weight:800;font-size:36px;line-height:27px;color:#111;text-transform:uppercase}
.meter-label{top:2188px;font-size:10px;letter-spacing:1px;color:#666}
.meter{left:83px;top:2206px;display:flex;gap:3px}
.meter i{width:12px;height:12px;border-radius:50%;background:#e4e4e4}
.meter i.on{background:var(--green)}
.perf-text{left:83px;top:2255px;width:500px;font-size:14px;line-height:21px;color:var(--text)}
.perf-text b{color:#111}
.perf-btn{left:82px;top:2336px;width:94px;height:40px;color:#111;font-weight:700}
.perf-photo{left:629px;top:2070px;width:468px;height:404px;background:var(--placeholder)}
.perf-photo .ph-label{left:116px;top:176px;font-size:60px}

/* stars */
.stars-photo{left:111px;top:2554px;width:451px;height:522px;background:var(--placeholder)}
.stars-photo .ph-label{left:114px;top:232px;font-size:60px}
.stars-title{left:611px;top:2676px;font-weight:800;font-size:36px;line-height:27px;color:var(--white);text-transform:uppercase}
.stars-text{left:611px;top:2812px;width:500px;font-size:14px;line-height:21px;color:#0b5d0b}
.stars-text b{color:#0a0a0a}
.stars-btn{left:610px;top:2893px;width:92px;height:39px;border-color:#0b6e0b;color:#0a3f0a;font-weight:700}

/* signup */
.signup-title{left:83px;top:3268px;font-weight:800;font-size:36px;line-height:27px;color:var(--white);text-transform:uppercase}
.signup-input{left:83px;top:3338px;width:202px;height:33px;background:var(--white);color:#888;font-size:10px;padding:9px 10px}
.signup-btn{left:292px;top:3338px;width:51px;height:33px;border:1px solid var(--green);color:var(--green);font-size:12px;display:flex;align-items:center;justify-content:center}
.signup-banner{left:464px;top:3270px;width:622px;height:119px;background:var(--placeholder)}
.signup-banner .ph-label{left:210px;top:40px;font-size:50px}

/* footer */
.site-footer{left:0;top:3460px;width:1200px;height:360px;background:var(--footer)}
.foot-col{top:3508px}
.foot-col h4{font-weight:500;font-size:15px;color:var(--white);margin-bottom:14px}
.foot-col a{display:block;font-size:11px;color:#5a8a5a;text-decoration:none;line-height:31px}
.foot-rule{left:0;top:3745px;width:1200px;height:1px;background:#333}
.copyright{left:83px;top:3776px;font-size:11px;color:#bbb}
.to-top{left:1075px;top:3763px;width:44px;height:44px;border:1px solid var(--green);transform:skewX(-20deg);display:flex;align-items:center;justify-content:center}
</style>
</head>
<body>
<div class="page">

  <svg class="backdrop" width="1200" height="3820" viewBox="0 0 1200 3820" aria-hidden="true">
    <defs>
      <linearGradient id="heroGrad" x1="0" y1="0" x2="0" y2="1">
        <stop offset="0" stop-color="#111"/>
        <stop offset=".4" stop-color="#2b2d2f"/>
        <stop offset="1" stop-color="#8b98a2"/>
      </linearGradient>
    </defs>
    <rect x="0" y="0" width="1200" height="1360" fill="url(#heroGrad)"/>
    <polygon points="890,620 1200,265 1200,1025 995,830" fill="#0a8c0a"/>
    <polygon points="0,1040 83,1080 83,1352 0,1345" fill="#138a13"/>
    <polygon points="0,1345 1200,1140 1200,1934 0,1934" fill="#dfe6e9"/>
    <rect x="0" y="2474" width="1200" height="140" fill="#f7f9fa"/>
    <polygon points="0,2632 1200,2498 1200,2662 0,2662" fill="#0d6b12"/>
    <polygon points="0,2632 600,2565 600,2662 0,2662" fill="#1c8c1c"/>
    <rect x="0" y="2662" width="1200" height="450" fill="#0cb00c"/>
    <rect x="0" y="3111" width="1200" height="350" fill="#1e1e1e"/>
    <polygon points="0,3111 1200,3111 1200,3140 0,3200" fill="#1b5c1b"/>
  </svg>

  <header class="site-header">
    <div class="brand"><span>BRAMWELL<br>HOCKEY</span><span class="mark"></span></div>
    <nav class="main-nav">
      <a class="active" href="#">Home</a><span class="sep"></span>
      <a href="#">Winter</a><span class="sep"></span>
      <a href="#">Spring</a><span class="sep"></span>
      <a href="#">Summer</a><span class="sep"></span>
      <a href="#">Team</a><span class="sep"></span>
      <a href="#">Tournament</a>
    </nav>
  </header>

  <div class="abs hero-photo" role="img" aria-label="Photograph of two ice hockey players battling for the puck"></div>
  <h1 class="abs hero-title">Focus<br>on your<br>purpose<span class="dot"></span></h1>
  <p class="abs hero-text">Per inceptos himenaeos. Mauris in erat justo. Nullam ac urna eu felis dapibus condimentum sit amet a augue. Sed non neque elit. Sed ut imperdiet nisi condimentum fermentum nunc. Etiam pharetra erat sed fermum feugiat, velit mauris egestas</p>
  <a class="abs btn-skew hero-btn"><span>Browse collection</span></a>
  <span class="abs partner" style="left:296px">Orbit</span>
  <span class="abs partner" style="left:382px">Stride</span>
  <div class="abs slider-dots"><i></i><i class="on"></i></div>

  <article class="abs category" style="left:83px;top:835px" role="img" aria-label="Skates category image">
    <span class="ph-label">576x400</span>
    <h3>Lorem ipsum dol mit samet</h3>
    <p>Etiam ullamcorper. Suspendisse a pellentesque dui, non felis. Maecenas malesuada elit lectus felis, male suada ultricies. Curabitur et ligula. Ut molestie.</p>
    <span class="see">See products</span>
  </article>
  <article class="abs category" style="left:610px;top:835px" role="img" aria-label="Sticks category image">
    <span class="ph-label">576x400</span>
    <h3>Cum sociis natoque penatibus</h3>
    <p>Phasellus fermentum in, dolor. Pellentesque facilisis. Nulla imperdiet sit amet magna. Vestibulum dapibus, mauris nec malesuada fames ac turpis</p>
    <span class="see">See products</span>
  </article>
  <article class="abs category dark" style="left:83px;top:1117px" role="img" aria-label="Protective gear category image">
    <span class="ph-label">576x400</span>
    <h3>Nulla ipsum dolor lacus suscipit</h3>
    <p><em>Aliquam erat ac ipsum. Integer aliquam purus. Qui</em> sque lorem tortor fringilla sed, vestibulum id, eleifend justo vel bibendum sapien massa ac turpis.</p>
    <span class="see">See products</span>
  </article>
  <article class="abs category" style="left:610px;top:1117px" role="img" aria-label="Helmets category image">
    <span class="ph-label">576x400</span>
    <h3>Ipsum primis in nibh vel risus</h3>
    <p>Integer ultrices posuere cubilia Curae, Nulla ipsum dolor lacus, suscipit adipiscing. Cum sociis nato penatibus et ultrices volutpat.</p>
    <span class="see">See products</span>
  </article>

  <h2 class="abs section-title">Learn more about us</h2>
  <div class="abs title-bar"></div>
  <p class="abs about-text">Per inceptos himenaeos. Mauris in erat justo. Nullam ac urna eu felis dapibus condimentum sit amet a augue. Sed non neque elit. Sed ut imperdiet nisi. Proin condimentu</p>

  <figure class="abs tile" style="left:93px">
    <div class="ph" role="img" aria-label="Academy training photo"><span class="ph-label">640x500</span></div>
    <figcaption class="caption">Aliquam eratac</figcaption>
    <span class="likes"><svg width="12" height="11" viewBox="0 0 24 22"><path d="M12 21 3 12a5 5 0 0 1 9-7 5 5 0 0 1 9 7z" fill="none" stroke="#0a9a0a" stroke-width="2"/></svg>41</span>
  </figure>
  <figure class="abs tile" style="left:436px">
    <div class="ph" role="img" aria-label="Coach on ice photo"><span class="ph-label">640x500</span></div>
    <figcaption class="caption">Quisque lorem tortor</figcaption>
    <span class="likes"><svg width="12" height="11" viewBox="0 0 24 22"><path d="M12 21 3 12a5 5 0 0 1 9-7 5 5 0 0 1 9 7z" fill="none" stroke="#0a9a0a" stroke-width="2"/></svg>53</span>
  </figure>
  <figure class="abs tile" style="left:779px">
    <div class="ph" role="img" aria-label="Team practice photo"><span class="ph-label">640x500</span></div>
    <figcaption class="caption">Curabitur et ligula</figcaption>
    <span class="likes"><svg width="12" height="11" viewBox="0 0 24 22"><path d="M12 21 3 12a5 5 0 0 1 9-7 5 5 0 0 1 9 7z" fill="none" stroke="#0a9a0a" stroke-width="2"/></svg>75</span>
  </figure>

  <div class="abs band" role="img" aria-label="Wide rink banner image"><span class="ph-label">1920x</span></div>

  <div class="abs perf-bg"></div>
  <h2 class="abs perf-title">Bring your<br>performance<br>to higher level</h2>
  <span class="abs meter-label" style="left:83px">YOUR PERFORMANCE</span>
  <span class="abs meter-label" style="left:352px">110%</span>
  <div class="abs meter"><i class="on"></i><i class="on"></i><i class="on"></i><i class="on"></i><i class="on"></i><i class="on"></i><i class="on"></i><i class="on"></i><i class="on"></i><i class="on"></i><i class="on"></i><i class="on"></i><i class="on"></i><i class="on"></i><i class="on"></i><i></i><i></i><i></i><i></i><i></i></div>
  <p class="abs perf-text"><b>Per inceptos himenaeos.</b> Mauris in erat justo. Nullam ac urna eu felis dapibus condimentum sit amet a augue.</p>
  <a class="abs btn-skew perf-btn"><span>Read more</span></a>
  <div class="abs perf-photo" role="img" aria-label="Player skating with the puck"><span class="ph-label">534x577</span></div>

  <div class="abs stars-photo" role="img" aria-label="Sport star supporting the academy"><span class="ph-label">515x594</span></div>
  <h2 class="abs stars-title">Meet<br>sport stars<br>who support<br>our mission</h2>
  <p class="abs stars-text">Curabitur placerat congue orci et maximus. Cras <b>ultrices semper congue</b>. Etiam molestie eu magna faucibus accumsan. Vivamus at auctor magna.</p>
  <a class="abs btn-skew stars-btn"><span>Read more</span></a>

  <h2 class="abs signup-title">Sign in to receive<br>new projects</h2>
  <div class="abs signup-input">Your email address</div>
  <div class="abs signup-btn">Ok</div>
  <div class="abs signup-banner" role="img" aria-label="Newsletter banner image"><span class="ph-label">707x136</span></div>

  <footer class="abs site-footer"></footer>
  <div class="abs foot-col" style="left:83px"><h4>Bibendum auctor</h4><a>Aenean ligula</a><a>Dapibus at dolor</a><a>Molestie id</a><a>Vestibulum</a><a>Aenean ligula</a></div>
  <div class="abs foot-col" style="left:346px"><h4>Class aptent</h4><a>Velit mauris</a><a>Entum feuis</a><a>Aliquam massa</a><a>Egestas quam</a></div>
  <div class="abs foot-col" style="left:610px"><h4>Vesti bulum</h4><a>Aenean ligula</a><a>Dapibus at dolor</a><a>Molestie id</a><a>Vestibulum</a><a>Aenean ligula</a></div>
  <div class="abs foot-col" style="left:874px"><h4>Egestas feuis</h4><a>Entum feuis</a><a>Aliquam massa</a><a>Egestas quam</a></div>
  <div class="abs foot-rule"></div>
  <p class="abs copyright">© 2023 Bramwell Hockey Academy</p>
  <a class="abs to-top" aria-label="Back to top"><svg width="16" height="10" viewBox="0 0 16 10" style="transform:skewX(20deg)"><path d="M1 9 8 2l7 7" fill="none" stroke="#fff" stroke-width="1.6"/></svg></a>

</div>
</body>
</html>
```